The Willowbrook Nest - a Nannying Agency for Corporate Companies and Professional Families

The Willowbrook Nest (www.thewillowbrooknest.com.au) is Australia's newest nannying agency aimed at corporate organisations and professional families.

I have attached 3 flyers previously designed that can be adapted if possible, or design 3 different flyers with different imaging that are edgy but professional selling the career opportunity or T.W.N. service. The flyers need to be double sided with image and company info on one side and service info on the other (which ill provide). Then the side with images needs to also be made smaller to be used as an advertisement in newsletters, Chatterbox, magazines etc.

Please provide Flyer 1 designs first, and then I will base my decision on this. The remaining 2 flyers will need to be provided by the winning designer after finishing up the 1st flyer design. Total prize money includes the design/source files for all 3 flyers.

Flyer 1 - Aimed at Families - Heading "Do You Need a Nanny - The Willowbrook Nest can help you find the balance?"
this is to advertise how our service can bring balance to family life and enable women to go back to work easily.
wording to state: The Willowbrook Nest is a nannying agency offering tailored child care services that meet the needs of professional families, while taking away the stress of on-boarding a nanny. If you want consistent family balance, good educational development and happy kids, come and join The Willowbrook Nest.
email address: findmeacarer@thewillowbrooknest.com.au
phone: 1300 864 239

Flyer 2 - Aimed at Nannies - Heading "Do You Want a Career As a Nanny?" this is to advertise a career as a nanny and be employed by The Willowbrook Nest.

The attached shows some wording changes to say
The Willowbrook Nest is Australia's newest nannying agency that recognises and rewards their employees, and provides supportive and structured career options in child care.
We offer full-time, part-time and holiday positions - if you want to have fun and be proud of the company you work for, come and join The Willowbrook Nest.
email address: joinourcarers@thewillowbrooknest.com.au
phone: 1300 864 239

Flyer 3 - Aimed at Companies - Heading "Want To Go Back To Work? The Willowbrook Nest can help you find a nanny"
Wording: The Willowbrook Nest is a nannying agency that enables organisations to support employees family life via employment benefit programs across Australia. Our tailored child care services meet the needs of professional families, while taking away the stress of on-boarding a nanny. If you want to provide family benefits to your employees
email address: hello@thewillowbrooknest.com.au
phone: 1300 864 239

Target Market(s)

Family and Company Flyers - Corporate Companies, Professional families, Mothers that want more time, wealthy business people - generally 30+ males and females
Nanny Flyer - people that love working with children, personal assistance, age brackets are 21 - 30 and 40+ males and females.

Industry/Entity Type

It Company

Font styles to use
Serif

Requirements
Must have
• Nanny Flyer - image of nannies promoting a happy, fun, professional culture - i will provide this image
Company Flyer - image could be a women showing 2 different lifestyles, one chaotic with kids, mess, showing guilt, tired, rushed life to childcare. Other half of life is organised, diary, laptop, Pocketel, corporate dress.
Family flyer - one side crazy disorganised, other side organised and balance family life
White background - navy blue font, align to our colour scheme and professional, shick image.
Should not have
• Should not use too much colour, comic illustrations.

```html
<!DOCTYPE html>
<html lang="en">
<head>
<meta charset="utf-8">
<title>The Willowbrook Nest – Family Flyer</title>
<link rel="stylesheet" href="https://fonts.googleapis.com/css2?family=PT+Sans+Narrow:wght@400;700&family=Libre+Baskerville&display=swap">
<style>
  :root {
    --navy: #1e1d50;
    --gold: #c8ab4c;
    --white: #ffffff;
    --grey-text: #55555f;
    --page: #eaeef0;
    --photo-light: #c9c9c9;
    --photo-mid: #8a8a8a;
    --photo-dark: #4a4a4a;
    --skin-light: #f3dccb;
    --hair: #9a6a43;
  }
  * { margin: 0; padding: 0; box-sizing: border-box; }
  html, body {
    width: 1098px;
    height: 1200px;
    overflow: hidden;
    background: var(--page);
  }
  .flyer {
    position: absolute;
    top: 206px;
    width: 510px;
    height: 788px;
    font-family: "PT Sans Narrow", "Arial Narrow", sans-serif;
    overflow: hidden;
    box-shadow: 0 12px 26px rgba(0, 0, 0, 0.18);
  }

  /* Front side */
  .flyer--front {
    left: 26px;
    background: var(--white);
    color: var(--navy);
    text-align: center;
  }
  .brand-name {
    position: absolute;
    left: 0; right: 0;
    top: 92px;
    font-family: "Libre Baskerville", Georgia, serif;
    font-size: 27px;
    letter-spacing: 1.5px;
    color: var(--navy);
  }
  .brand-tagline {
    position: absolute;
    left: 0; right: 0;
    top: 136px;
    font-family: "Libre Baskerville", Georgia, serif;
    font-size: 14px;
    letter-spacing: 0.5px;
    color: var(--grey-text);
  }
  .headline-lead {
    position: absolute;
    left: 0; right: 0;
    top: 170px;
    font-size: 46px;
    font-weight: 700;
    color: var(--gold);
    line-height: 1;
  }
  .headline-main {
    position: absolute;
    left: 0; right: 0;
    top: 214px;
    font-size: 122px;
    font-weight: 700;
    line-height: 1;
    letter-spacing: 2px;
    color: var(--navy);
  }
  .headline-sub {
    position: absolute;
    left: 30px; right: 30px;
    top: 346px;
    font-size: 32px;
    line-height: 38px;
    color: var(--gold);
  }
  .child-photo {
    position: absolute;
    left: 0;
    top: 442px;
    width: 510px;
    height: 300px;
    background: radial-gradient(ellipse at 30% 45%, var(--skin-light) 0%, #eadbd0 40%, var(--white) 75%),
                var(--white);
  }
  .child-photo::before {
    content: "";
    position: absolute;
    left: 20px;
    top: 40px;
    width: 120px;
    height: 160px;
    border-radius: 50%;
    background: radial-gradient(ellipse, var(--hair) 0%, rgba(154,106,67,0) 70%);
  }
  .front-band {
    position: absolute;
    left: 0;
    bottom: 0;
    width: 510px;
    height: 46px;
    background: var(--navy);
  }

  /* Info side */
  .flyer--info {
    left: 562px;
    background: var(--navy);
    color: var(--white);
  }
  .family-photo {
    position: absolute;
    left: 0;
    top: 0;
    width: 510px;
    height: 310px;
    background: radial-gradient(ellipse at 50% 45%, var(--photo-light) 0%, var(--photo-mid) 55%, var(--photo-dark) 100%);
  }
  .photo-wave {
    position: absolute;
    left: 0;
    top: 0;
    width: 510px;
    height: 310px;
  }
  .intro {
    position: absolute;
    left: 37px;
    right: 33px;
    top: 326px;
    font-size: 23px;
    line-height: 34px;
    text-align: justify;
  }
  .intro strong {
    font-weight: 700;
    font-size: 27px;
  }
  .contact-band {
    position: absolute;
    left: 0;
    width: 510px;
    display: flex;
    align-items: center;
  }
  .contact-band svg { flex: none; }
  .contact-band--email {
    top: 624px;
    height: 46px;
    background: var(--gold);
    padding-left: 37px;
    gap: 22px;
    font-size: 21px;
  }
  .contact-band--phone {
    top: 670px;
    height: 70px;
    padding-left: 44px;
    gap: 24px;
  }
  .phone-number {
    color: var(--gold);
    font-weight: 700;
    font-size: 42px;
    letter-spacing: 4.5px;
  }
  .contact-band--web {
    top: 740px;
    height: 48px;
    background: var(--gold);
    padding-left: 37px;
    gap: 40px;
    font-size: 21px;
  }
</style>
</head>
<body>
  <article class="flyer flyer--front">
    <p class="brand-name">THE WILLOWBROOK NEST</p>
    <p class="brand-tagline">Professional Nanny Agency</p>
    <h1>
      <span class="headline-lead">Do You Need a</span>
      <span class="headline-main">NANNY</span>
    </h1>
    <p class="headline-sub">The Willowbrook Nest can help you find the balance?</p>
    <div class="child-photo" role="img" aria-label="Photo of a young girl with pigtails peeking in from the side"></div>
    <div class="front-band"></div>
  </article>

  <article class="flyer flyer--info">
    <div class="family-photo" role="img" aria-label="Black and white photo of a smiling family with two young daughters sitting in front of a camping tent with a map"></div>
    <svg class="photo-wave" viewBox="0 0 510 310" aria-hidden="true">
      <path d="M0,290 C130,306 300,296 510,274 L510,310 L0,310 Z" fill="var(--navy)"/>
    </svg>

    <p class="intro">The Willowbrook Nest is a nannying agency offering tailored child care services that meet the needs of professional families, while taking away the stress of on-boarding a nanny. If you want consistent family balance, good educational development and happy kids, <strong>come and join The Willowbrook Nest.</strong></p>

    <div class="contact-band contact-band--email">
      <svg width="34" height="23" viewBox="0 0 44 30" aria-hidden="true">
        <rect x="1.5" y="1.5" width="41" height="27" fill="none" stroke="#fff" stroke-width="2.5"/>
        <path d="M1.5,1.5 L22,17 L42.5,1.5" fill="none" stroke="#fff" stroke-width="2.5"/>
      </svg>
      <span class="contact-text">findmeacarer@thewillowbrooknest.com.au</span>
    </div>

    <div class="contact-band contact-band--phone">
      <svg width="26" height="38" viewBox="0 0 34 50" aria-hidden="true">
        <path d="M10,2 L16,14 L11,19 C13,27 17,33 23,38 L28,33 L33,43 L26,48 C12,42 3,26 3,8 Z" fill="#fff"/>
      </svg>
      <span class="phone-number">1300 864 239</span>
    </div>

    <div class="contact-band contact-band--web">
      <svg width="30" height="30" viewBox="0 0 36 36" aria-hidden="true">
        <g fill="none" stroke="#fff" stroke-width="2.2">
          <circle cx="18" cy="18" r="16"/>
          <ellipse cx="18" cy="18" rx="7" ry="16"/>
          <line x1="18" y1="2" x2="18" y2="34"/>
          <line x1="2" y1="18" x2="34" y2="18"/>
          <path d="M5,9 H31 M5,27 H31"/>
        </g>
      </svg>
      <span class="contact-text">www.thewillowbrooknest.com.au</span>
    </div>
  </article>
</body>
</html>
```